Banner for home page on event planning site

We are revamping the home page www.harborlanecelebrations.com and would like to add a banner to the center of it to guide potential clients to one of 3 areas of the site:

Weddings, Corporate Events, Parties and More

I'm uploading an attachment that shows where the banner will be placed. It needs to have those 3 distinct sections, and match the existing colors/branding of the site. The fonts used for the logo are Lucida Bright and Callie Hand. Both are available for free.

Please use lorem ipsum under each section, I'll fill that in later. It should just be highly designed, beautiful, and easy to understand that clicking these will take you to the different areas of the site.
Updates

Hi designers,
Here are some problems we are having with the designs that have been submitted.
1) 3 stock images as squares... when you do this and then put it into the existing website, it gets lost among the other boxes. We need this to be where the eye goes immediately when you land on the site.
2) Not enough of a frame or white space... we think you need some white space to make this stand out as different from the surrounding area.
3) No clearly defined areas. It needs to be easy for people to figure out... Weddings, click here. Parties, click here. Corporate events, click here.

Industry/Entity Type

Event Planning

Requirements
Should not have
• Nothing with orchids, her competitor uses them and they are common in the event planning industry. We want to stay away from them.

```html
<!DOCTYPE html>
<html lang="en">
<head>
<meta charset="utf-8">
<title>Harbor Lane Celebrations — Event Sections Banner</title>
<link rel="stylesheet" href="https://fonts.googleapis.com/css2?family=Parisienne&family=Noticia+Text&display=swap">
<style>
  :root {
    --frame-magenta: #b44a8c;
    --panel-gold: #c9b866;
    --panel-gold-light: #d2c37a;
    --heading-pink: #c2509a;
    --body-grey: #6b6472;
  }
  * { box-sizing: border-box; margin: 0; padding: 0; }
  html, body { width: 1200px; height: 1000px; overflow: hidden; }
  body { background: var(--frame-magenta); }
  .banner { position: relative; width: 1200px; height: 1000px; }
  .section-panel {
    position: absolute; top: 20px; height: 960px;
    overflow: hidden; color: var(--body-grey);
    text-decoration: none; display: block;
  }
  .section-panel--weddings { left: 20px; width: 367px; }
  .section-panel--corporate { left: 407px; width: 384px; }
  .section-panel--parties { left: 811px; width: 369px; }
  .panel-texture {
    position: absolute; inset: 0;
    background: radial-gradient(circle at 50% 40%, var(--panel-gold-light), var(--panel-gold) 75%);
  }
  .section-title {
    position: relative;
    font-family: "Parisienne", cursive;
    font-weight: 400;
    color: var(--heading-pink);
    font-size: 66px;
    line-height: 84px;
    text-align: center;
  }
  .section-panel--weddings .section-title { padding-top: 44px; letter-spacing: 2px; }
  .section-panel--corporate .section-title,
  .section-panel--parties .section-title { padding-top: 30px; letter-spacing: 1px; }
  .section-copy {
    position: absolute; left: 15px;
    font-family: "Noticia Text", serif;
    font-size: 13.2px; line-height: 19px;
    white-space: nowrap;
  }
  .section-panel--weddings .section-copy { top: 184px; }
  .section-panel--corporate .section-copy,
  .section-panel--parties .section-copy { left: 25px; top: 203px; }
  .section-panel--parties .section-copy { left: 19px; }
  .section-copy p + p { margin-top: 19px; }
</style>
</head>
<body>
<main class="banner">

  <a class="section-panel section-panel--weddings" href="#weddings">
    <div class="panel-texture" role="img" aria-label="Faint tone-on-tone daisy pattern on gold"></div>
    <h2 class="section-title">Weddings</h2>
    <div class="section-copy">
      <p>Lorem ipsum dolor sit amet,<br>an bonorum percipit expetendis sit.<br>Natum choro consectetuer ei nam,<br>et eum tale dicit aliquando. Semper<br>delectus sed ei. Mazim facete ad mei,<br>ei dico doctus vel, facilis eloquentiam<br>eu per. Ex vide omnis interesset quo, sint<br>epicuri cum ex.</p>
      <p>Vix probo facete malorum eu, id reque<br>diceret pro. Noster eirmod comprehensam<br>eum id, est te graeco feugait. Cu eam<br>equidem epicuri necessitatibus. Graecis<br>fabellas corrumpit sea eu. Usu eu quod<br>scriptorem. Ex modus fabellas usu,<br>phaedrum similique intellegam sit te.</p>
      <p>Nominati eloquentiam sea in. Cu nonumy<br>atomorum delicata pro. Mei possit definitiones<br>ut, iudicabit moderatius id quo. Ius ne error<br>persecuti, dico gloriatur ex nec. Mei summo<br>aliquid id, eu tale oblique liberavisse quo.<br>Mea fugit scribentur theophrastus cu.</p>
      <p>Eum officiis splendide definitiones at.<br>No mei congue consulatu neglegentur,<br>aperiri malorum sit eu, qui ea feugiat assentior.<br>Ut pri vero ornatus dolorum. No purto facilisis<br>iracundia vim, decore legimus nam no. Est vidit<br>utinam ea. Vis ex homero quodsi tractatos.</p>
      <p>Eam facer postulant et. Id tantas vocent vis,<br>doming diceret accumsan mea ad. Eum no<br>aeque appetere nominati, ex mei integre periculis.<br>Erant solet reprimique pro ut, eu virtute accommodare<br>his. At viris facilisi mel, his omnis partem elaboraret cu.<br>Ut perfecto facilisis sed. Cum scaevola corrumpit at,<br>eum invenire conclusionemque no, sed quaeque<br>consetetur eu.</p>
    </div>
  </a>

  <a class="section-panel section-panel--corporate" href="#corporate-events">
    <div class="panel-texture" role="img" aria-label="Faint tone-on-tone daisy pattern on gold"></div>
    <h2 class="section-title">Corporate<br>Events</h2>
    <div class="section-copy">
      <p>Lorem ipsum dolor sit amet,<br>an bonorum percipit expetendis sit.<br>Natum choro consectetuer ei nam,<br>et eum tale dicit aliquando. Semper<br>delectus sed ei. Mazim facete ad mei,<br>ei dico doctus vel, facilis eloquentiam<br>eu per. Ex vide omnis interesset quo, sint<br>epicuri cum ex.</p>
      <p>Vix probo facete malorum eu, id reque<br>diceret pro. Noster eirmod comprehensam<br>eum id, est te graeco feugait. Cu eam<br>equidem epicuri necessitatibus. Graecis<br>fabellas corrumpit sea eu. Usu eu quod<br>scriptorem. Ex modus fabellas usu,<br>phaedrum similique intellegam sit te.</p>
      <p>Nominati eloquentiam sea in. Cu nonumy<br>atomorum delicata pro. Mei possit definitiones<br>ut, iudicabit moderatius id quo. Ius ne error<br>persecuti, dico gloriatur ex nec. Mei summo<br>aliquid id, eu tale oblique liberavisse quo.<br>Mea fugit scribentur theophrastus cu.</p>
      <p>Eum officiis splendide definitiones at.<br>No mei congue consulatu neglegentur,<br>aperiri malorum sit eu, qui ea feugiat assentior.<br>Ut pri vero ornatus dolorum. No purto facilisis<br>iracundia vim, decore legimus nam no. Est vidit<br>utinam ea. Vis ex homero quodsi tractatos.</p>
      <p>Eam facer postulant et. Id tantas vocent vis,<br>doming diceret accumsan mea ad. Eum no<br>aeque appetere nominati, ex mei integre periculis.<br>Erant solet reprimique pro ut, eu virtute accommodare<br>his. At viris facilisi mel, his omnis partem elaboraret cu.<br>Ut perfecto facilisis sed. Cum scaevola corrumpit at,<br>eum invenire conclusionemque no, sed quaeque<br>consetetur eu.</p>
    </div>
  </a>

  <a class="section-panel section-panel--parties" href="#parties-and-more">
    <div class="panel-texture" role="img" aria-label="Faint tone-on-tone daisy pattern on gold"></div>
    <h2 class="section-title">Parties<br>and More</h2>
    <div class="section-copy">
      <p>Lorem ipsum dolor sit amet,<br>an bonorum percipit expetendis sit.<br>Natum choro consectetuer ei nam,<br>et eum tale dicit aliquando. Semper<br>delectus sed ei. Mazim facete ad mei,<br>ei dico doctus vel, facilis eloquentiam<br>eu per. Ex vide omnis interesset quo, sint<br>epicuri cum ex.</p>
      <p>Vix probo facete malorum eu, id reque<br>diceret pro. Noster eirmod comprehensam<br>eum id, est te graeco feugait. Cu eam<br>equidem epicuri necessitatibus. Graecis<br>fabellas corrumpit sea eu. Usu eu quod<br>scriptorem. Ex modus fabellas usu,<br>phaedrum similique intellegam sit te.</p>
      <p>Nominati eloquentiam sea in. Cu nonumy<br>atomorum delicata pro. Mei possit definitiones<br>ut, iudicabit moderatius id quo. Ius ne error<br>persecuti, dico gloriatur ex nec. Mei summo<br>aliquid id, eu tale oblique liberavisse quo.<br>Mea fugit scribentur theophrastus cu.</p>
      <p>Eum officiis splendide definitiones at.<br>No mei congue consulatu neglegentur,<br>aperiri malorum sit eu, qui ea feugiat assentior.<br>Ut pri vero ornatus dolorum. No purto facilisis<br>iracundia vim, decore legimus nam no. Est vidit<br>utinam ea. Vis ex homero quodsi tractatos.</p>
      <p>Eam facer postulant et. Id tantas vocent vis,<br>doming diceret accumsan mea ad. Eum no<br>aeque appetere nominati, ex mei integre periculis.<br>Erant solet reprimique pro ut, eu virtute accommodare<br>his. At viris facilisi mel, his omnis partem elaboraret cu.<br>Ut perfecto facilisis sed. Cum scaevola corrumpit at,<br>eum invenire conclusionemque no, sed quaeque<br>consetetur eu.</p>
    </div>
  </a>

</main>
</body>
</html>
```